Business card design for web travel company

Hi
we'd like to receive some proposal for a business card design.
Stayvano is a private travel club, dedicated to all travel lovers, with unique offers for exclusive destinations all around the world. At Stayvano you can find a wide range of offers for resorts, boutique hotels and travel packages at the best guaranteed price available on the market. The convenience of the offer is guaranteed by a private sales model: offers are available for a limited time only and they are personally chosen by Stayvano's qualified team of travel experts.
We offer only exclusive hotels with discounted prices but we are not an outlet or a discount supermarket: the design should reflect our connection with luxury, exclusivity using the same style of our website www.stayvano-example.com.
We want to make sure that when we'll present ourself to our business partner they will feel immediately which is our brand positioning giving them also a sense of an affordable and reliable partner.
In attachment you can also find our brand guidelines (please note that we are NOT USING ANY MORE THE TAG LINE "Five star outlet" mentioned in it).
The info to be inserted are:
Name Surname
Job Title
Tel
Mobile (when needed)
Email
Stayvano S.r.l.
Via Bruno Lesta 27
20131 Milano

```html
<!DOCTYPE html>
<html lang="en">
<head>
<meta charset="utf-8">
<title>Stayvano – Business Card</title>
<link href="https://fonts.googleapis.com/css2?family=Carlito:wght@400;700&display=swap" rel="stylesheet">
<style>
  :root {
    --page: #ffffff;
    --card-black: #000000;
    --card-charcoal: #141414;
    --olive-dark: #767400;
    --olive-light: #c9c800;
    --lime-bright: #f2f26a;
    --ink-dark: #1a1a00;
    --ink-light: #ffffff;
  }
  html, body {
    margin: 0;
    width: 1200px;
    height: 900px;
    overflow: hidden;
    background: var(--page);
    font-family: "Carlito", "Calibri", sans-serif;
  }
  .canvas {
    position: relative;
    width: 1200px;
    height: 900px;
  }
  .card {
    position: absolute;
    top: 294px;
    width: 544px;
    height: 310px;
    overflow: hidden;
    box-shadow: 0 0 8px rgba(0, 0, 0, 0.35);
  }
  .card--front { left: 29px; background: linear-gradient(135deg, var(--card-charcoal), var(--card-black)); }
  .card--back { left: 628px; background: var(--card-black); }

  .front-bands { position: absolute; inset: 0; }

  .brand-name {
    position: absolute;
    left: 0;
    right: 0;
    top: 48px;
    margin: 0;
    text-align: center;
    font-weight: 400;
    font-size: 86px;
    letter-spacing: 1px;
    line-height: 1;
    color: var(--ink-light);
  }
  .front-contact {
    position: absolute;
    left: 0;
    right: 0;
    top: 251px;
    margin: 0;
    text-align: center;
    font-size: 15px;
    line-height: 22px;
    color: var(--ink-dark);
  }
  .front-contact .sep { margin: 0 6px; }

  .contact-list {
    position: absolute;
    left: 35px;
    top: 177px;
    margin: 0;
    padding: 0;
    list-style: none;
  }
  .contact-list li {
    display: flex;
    align-items: center;
    height: 36px;
    font-size: 17.5px;
    color: var(--ink-light);
  }
  .contact-list .bullet {
    width: 16px;
    height: 16px;
    margin-right: 12px;
    background: linear-gradient(135deg, var(--olive-dark), var(--lime-bright) 60%, var(--olive-light));
  }
</style>
</head>
<body>
<main class="canvas">
  <section class="card card--front" aria-label="Card front">
    <svg class="front-bands" width="544" height="310" viewBox="0 0 544 310" aria-hidden="true">
      <defs>
        <linearGradient id="olive-field" x1="0" y1="0" x2="1" y2="0">
          <stop offset="0" stop-color="var(--olive-dark)"/>
          <stop offset="1" stop-color="var(--olive-light)"/>
        </linearGradient>
        <linearGradient id="lime-strip" x1="0" y1="0" x2="1" y2="0">
          <stop offset="0" stop-color="#a8a600"/>
          <stop offset="0.75" stop-color="var(--lime-bright)"/>
          <stop offset="1" stop-color="#e0e030"/>
        </linearGradient>
      </defs>
      <rect x="0" y="222" width="544" height="88" fill="url(#olive-field)"/>
      <polygon points="0,200 544,211 544,222 0,222" fill="url(#lime-strip)"/>
      <rect x="0" y="220" width="544" height="3" fill="#000" opacity="0.35"/>
    </svg>
    <h1 class="brand-name">Stayvano</h1>
    <p class="front-contact">
      Stayvano S.r.l., Via Bruno Lesta 27, 20131 Milano<br>
      M. 0298765431<span class="sep">•</span>E. hello@stayvano-example.com
    </p>
  </section>

  <section class="card card--back" aria-label="Card back">
    <ul class="contact-list">
      <li><span class="bullet"></span>Stayvano S.r.l., Via Bruno Lesta 27, 20131 Milano</li>
      <li><span class="bullet"></span>M. 0298765431</li>
      <li><span class="bullet"></span>E. hello@stayvano-example.com</li>
    </ul>
  </section>
</main>
</body>
</html>
```